Bref créative
Business Cards, Gift Bag, Shirt and More
Quietly Marigold Treasures
Use same font as used in my logo
None to be used
742 Orchard Lane
Dunmore, KS 67402-2814
clerk@prairiekinfolkwellness.example
www.quietlymarigoldtreasures.example and www.prairiekinfolkwellness.example
We have a premier gift store called Quietly Marigold Treasures. The gift store is located inside of Prairie Kinfolk Wellness, a retail Pharmacy and Home Care store. We love the sunflower in our logo and also love the look of paisley and damask prints. This is the kind of elegance and classiness we are looking for.
Fonts – Please try a different font for the word GIFT.
Business Cards – Include wording: Division of PRAIRIE KINFOLK WELLNESS on back of card. On front or back include wording: Quietly the Finest Wedding Registry, Quietly the Finest Loyalty Rewards, Quietly the Finest Gifts. Needs to be room for employees to write their name on the cards either on front or back (no preprinted names or titles on cards).
Letterhead and Fax – Please include on bottom the wording: Division of PRAIRIE KINFOLK WELLNESS.
Envelope – On the back flap – Please include the wording: Division of PRAIRIE KINFOLK WELLNESS.
Sign – Sign holder dimension is 2’3” tall by 10’0” wide – illuminated at night. This sign will be located near our Prairie Kinfolk Wellness sign on the exterior of our building.
Gift Bags – Design on the bag should be only one color. We are considering using chocolate brown or black bags with Metallic Gold or Metallic Bronze for the logo color.
Front and Back Design for Hang Tags – Round Circle or Oval design. There must be enough room on the back of the hang tag for us to place a 1.75” wide x .5” tall bar code sticker. Back side needs to be white. Needs to have a small hole punch to hang with string or ribbon.
Stickers/Seals – A simple round seal that we can use to seal tissue paper when putting products in gift bags.
Front Side of a Loyalty Reward Card Design –Prairie Kinfolk Wellness Logo, Quietly Marigold Treasures Logo and the words LOYALTY REWARDS.
Top of Coupon for Loyalty Reward Program – All information needs to fit in the top 1 ½ inches of a standard 8 ½ x 11 paper. Information needed – Prairie Kinfolk Wellness logo, Quietly Marigold Treasures and the words LOYALTY REWARDS.
Shirts – Please add Prairie Kinfolk Wellness Logo to design somehow – perhaps on the sleeve. Consider using a damask or paisley black or rich chocolate brown print for the design.
Thank You!
Quietly Marigold Treasures logo
Prairie Kinfolk Wellness logo
Sample for loyalty rewards coupon

```html
<!DOCTYPE html>
<html lang="en">
<head>
<meta charset="utf-8">
<title>Quietly Marigold Treasures – Business Card</title>
<link rel="stylesheet" href="https://fonts.googleapis.com/css2?family=Cinzel:wght@500&family=Tinos:wght@400&display=swap">
<style>
  :root {
    --backdrop: #2b2b2b;
    --card: #ffffff;
    --gold: #e2a920;
    --band-gold: #e8b52a;
    --ink: #1f1f1f;
    --rule-orange: #e39b3a;
    --leaf-green: #8dbb3a;
    --chocolate: #6b3a1f;
    --flower-soft: #f6ecc4;
    --flower-leaf: #eef3de;
  }
  * { box-sizing: border-box; margin: 0; padding: 0; }
  html, body { width: 1200px; height: 901px; overflow: hidden; }
  body {
    background: var(--backdrop);
    display: flex;
    flex-direction: column;
    align-items: center;
    justify-content: center;
    gap: 30px;
  }
  .card {
    position: relative;
    width: 720px;
    height: 411px;
    background: var(--card);
    overflow: hidden;
    font-family: "Tinos", "Times New Roman", serif;
    color: var(--ink);
  }
  .wordmark {
    position: absolute;
    display: flex;
    align-items: center;
    gap: 12px;
    font-family: "Cinzel", serif;
    font-weight: 500;
    color: var(--gold);
    white-space: nowrap;
  }
  .wordmark .dot {
    width: 24px; height: 24px;
    border-radius: 50%;
    background: var(--gold);
    flex: none;
  }
  .flower-decor {
    position: absolute;
    border-radius: 50%;
    background: radial-gradient(circle at 50% 45%, var(--flower-soft) 0 38%, var(--flower-leaf) 60%, rgba(255,255,255,0) 72%);
  }

  /* back */
  .card-back .flower-decor { left: 40px; top: 20px; width: 360px; height: 360px; }
  .card-back .wordmark { left: 100px; top: 152px; font-size: 30px; }
  .card-back .division {
    position: absolute;
    left: 136px; top: 212px;
    padding: 5px 18px;
    border: 2px solid var(--rule-orange);
    font-size: 17px;
    letter-spacing: 0.04em;
  }
  .card-back .site {
    position: absolute;
    right: 30px; top: 26px;
    font-size: 14px;
    color: var(--leaf-green);
  }

  /* front */
  .card-front .flower-decor { right: -40px; top: -10px; width: 380px; height: 380px; }
  .card-front .wordmark { left: 36px; top: 46px; font-size: 30px; }
  .contact { position: absolute; left: 40px; top: 140px; font-size: 15px; line-height: 1.3; }
  .contact .lines { margin-top: 22px; }
  .tagline {
    position: absolute;
    left: 40px; top: 284px;
    padding: 3px 8px;
    border: 2px solid var(--rule-orange);
    font-size: 14px;
    white-space: nowrap;
  }
  .swatches { position: absolute; right: 0; top: 322px; display: flex; height: 24px; }
  .swatch-brown { width: 40px; background: var(--chocolate); }
  .swatch-green { width: 40px; background: var(--leaf-green); }
  .swatch-band {
    width: 210px;
    background: var(--leaf-green);
    color: #fff;
    font-size: 11px;
    line-height: 24px;
    padding-left: 8px;
    margin-left: 6px;
    white-space: nowrap;
  }
  .footer-band {
    position: absolute;
    left: 0; right: 0; bottom: 0;
    height: 56px;
    background: var(--band-gold);
    color: #fff;
    font-size: 18px;
    letter-spacing: 0.05em;
    padding: 16px 40px;
  }
</style>
</head>
<body>

  <section class="card card-back" aria-label="Business card back">
    <div class="flower-decor" role="img" aria-label="Faint sunflower illustration"></div>
    <div class="site">www.prairiekinfolkwellness.example</div>
    <div class="wordmark"><span class="dot"></span>Quietly Marigold Treasures</div>
    <div class="division">Division of PRAIRIE KINFOLK WELLNESS</div>
  </section>

  <section class="card card-front" aria-label="Business card front">
    <div class="flower-decor" role="img" aria-label="Faint sunflower illustration"></div>
    <div class="wordmark"><span class="dot"></span>Quietly Marigold Treasures</div>
    <div class="contact">
      <p>742 Orchard Lane</p>
      <p>Dunmore, KS 67402-2814</p>
      <div class="lines">
        <p>P: (785) 555-0142</p>
        <p>F: (785) 555-0187</p>
        <p>E: clerk@prairiekinfolkwellness.example</p>
      </div>
    </div>
    <div class="tagline">Quietly the Finest Wedding Registry, Quietly the Finest Loyalty Rewards, Quietly the Finest Gifts.</div>
    <div class="swatches">
      <span class="swatch-brown"></span>
      <span class="swatch-green"></span>
      <span class="swatch-band">www.prairiekinfolkwellness.example</span>
    </div>
    <div class="footer-band">www.quietlymarigoldtreasures.example</div>
  </section>

</body>
</html>
```